Vegetable Grower Expo Backdrop

I need an 8x8 backdrop for an expo booth. We are a vegetable grower and have very limited graphics to work with. I have uploaded our logo which may not be the correct format and need to be updated for quality to print at that size. Need something quick and simple. Expo is August 18th

Target Market(s)

Retail and Wholesale buyers

Industry/Entity Type

Produce

Colors

Designer to choose colors to be used in the design.

Requirements
Must have
• Logo
Nice to have
• I am open to ideas!
Should not have
• Keep it simple and bottom 1/4 will be covered with samples so focus on top 3/4 of banner

```html
<!DOCTYPE html>
<html lang="en">
<head>
<meta charset="utf-8">
<title>Vegetable Grower Expo 2025 Backdrop</title>
<link rel="stylesheet" href="https://fonts.googleapis.com/css2?family=Poppins:wght@500;600&family=Archivo:wght@700&display=swap">
<style>
  :root {
    --forest: #07421f;
    --lime: #b3d335;
    --lime-soft: #c9e06a;
    --pale: #eef3dc;
    --white: #ffffff;
  }
  * { margin: 0; padding: 0; box-sizing: border-box; }
  html, body { width: 721px; height: 1200px; overflow: hidden; }
  body { background: var(--forest); position: relative; font-family: "Poppins", sans-serif; }

  .backdrop {
    position: absolute; left: 143px; top: 69px;
    width: 435px; height: 436px;
    background: var(--white);
    box-shadow: 0 10px 10px rgba(0,0,0,0.25);
  }
  .cell { position: absolute; width: 105px; }

  .headline {
    position: absolute; left: 24px; top: 22px; height: 178px; width: 60px;
    writing-mode: vertical-rl; transform: rotate(180deg);
    font-family: "Archivo", sans-serif; font-weight: 700;
    font-size: 29px; line-height: 29px; letter-spacing: 0.2px;
    color: var(--lime); text-align: left;
  }

  .expo-tag {
    left: 110px; top: 0; height: 111px; background: var(--pale);
    display: flex; flex-direction: column; justify-content: center; padding-left: 11px;
    font-weight: 600; font-size: 33px; line-height: 27px; letter-spacing: -0.5px;
  }
  .expo-tag .word { color: var(--forest); }
  .expo-tag .year { color: var(--lime); }

  .brand-name {
    position: absolute; left: 237px; top: 30px; width: 190px; height: 52px;
    display: flex; flex-direction: column; justify-content: center;
    font-weight: 600; font-size: 21px; line-height: 24px; letter-spacing: 0.3px;
    color: var(--forest);
  }

  .photo { height: 105px; }
  .photo-deep { background: linear-gradient(135deg, #0e5528, #083d1c); }
  .photo-fresh { background: linear-gradient(135deg, #cde48a, #a9d14d 55%, #e5a13a); }
  .photo-citrus { background: linear-gradient(135deg, #c7dc6a, #e79a2e 55%, #9cc43e); }
  .photo-greens { background: linear-gradient(135deg, #6fae2c, #e6ecd0 45%, #e4892b 75%, #3f7c22); }
  .photo-market { background: linear-gradient(135deg, #d9c27a, #f0a823 35%, #c8362a 65%, #7bbf3c); }
  .photo-harvest { background: linear-gradient(135deg, #d64a2a, #f2c42e 45%, #7fae2f 70%, #4a2a4a); }

  .expo-band {
    left: 220px; top: 326px; height: 110px; background: var(--lime);
    display: flex; flex-direction: column; justify-content: center; align-items: center;
    font-weight: 500; font-size: 36px; line-height: 30px; letter-spacing: -0.5px;
    color: var(--lime-soft);
  }
</style>
</head>
<body>
  <main class="backdrop">
    <h1 class="headline">VEGETABLE<br>GROWER</h1>

    <div class="cell expo-tag">
      <span class="word">EXPO</span>
      <span class="year">2025</span>
    </div>

    <p class="brand-name">MAPLE RIDGE<br>FARMS</p>

    <div class="cell photo photo-deep" style="left:110px; top:111px" role="img" aria-label="Mixed vegetables under a dark green tint"></div>
    <div class="cell photo photo-fresh" style="left:220px; top:111px" role="img" aria-label="Lettuce, pears, apples and peppers"></div>
    <div class="cell photo photo-citrus" style="left:330px; top:111px" role="img" aria-label="Tomatoes, avocado, celery and lemon"></div>

    <div class="cell photo photo-greens" style="left:0; top:221px" role="img" aria-label="Lettuce, garlic, carrots and cabbage"></div>
    <div class="cell photo photo-deep" style="left:110px; top:221px" role="img" aria-label="Apples and vegetables under a dark green tint"></div>
    <div class="cell photo photo-market" style="left:220px; top:221px" role="img" aria-label="Potatoes, yellow pepper, tomatoes and apples"></div>
    <div class="cell photo photo-harvest" style="left:330px; top:221px" role="img" aria-label="Tomatoes, grapefruit, broccoli and eggplant"></div>

    <div class="cell expo-band" aria-hidden="true">
      <span>EXPO</span>
      <span>2025</span>
      <span>EXPO</span>
    </div>
  </main>
</body>
</html>
```